Template für Webova-Page
Zielgruppe
Geschlecht: ca. 90% Männlich
Alter: ca. 30-60 Jahre
höheres Einkommen, höhere Bildung
Aufgabenstellung
FORNVALT ist ein Netzwerk von Maßschuhmachern. Die Schuhmacher werden auf der Webseite gefunden und es wird ein Eindruck der Möglichkeiten des Maßschuhmachens vermittelt.
Aufgrund der offenen Struktur arbeiten wir derzeit mit Webova, damit jeder Schuhmacher die Möglichkeit hat, Inhalte einzustellen, zu pflegen und zu aktualisieren.
Webova scheint für diese Zwecke gut geeignet, hat aber kein adäquates Standard-Layout.
ES GEHT NUR UM DAS WEBDESIGN, NICHT UM DIE IMPLEMENTIERUNG!

```html
<!DOCTYPE html>
<html lang="de">
<head>
<meta charset="utf-8">
<title>FORNVALT – Maßschuhe à la carte</title>
<link href="https://fonts.googleapis.com/css2?family=Arimo:wght@400;700&display=swap" rel="stylesheet">
<style>
  :root {
    --bg-dark: #0d0d0d;
    --bg-mid: #1e1e1e;
    --bg-light: #2a2a2a;
    --panel-a: #262626;
    --panel-b: #1c1c1c;
    --panel-edge: #2e2e2e;
    --bar-top: #2f3032;
    --bar-bottom: #151617;
    --gold: #cba84c;
    --text: #ececec;
    --muted: #b8b8b8;
    --divider: #3a3a3a;
    --photo-top: #5a4a45;
    --photo-mid: #a89388;
    --photo-low: #d8cfc8;
  }
  * { box-sizing: border-box; margin: 0; padding: 0; }
  html, body { width: 1200px; height: 945px; overflow: hidden; }
  body {
    position: relative;
    font-family: "Arimo", Arial, sans-serif;
    color: var(--text);
    letter-spacing: 0.05em;
    background:
      radial-gradient(ellipse 420px 300px at 15% 20%, rgba(60,60,60,.35), transparent 70%),
      radial-gradient(ellipse 500px 380px at 85% 70%, rgba(55,55,55,.3), transparent 70%),
      radial-gradient(ellipse 380px 280px at 40% 95%, rgba(50,50,50,.3), transparent 70%),
      radial-gradient(ellipse at 50% 45%, var(--bg-mid), var(--bg-dark) 80%);
  }
  .brand {
    position: absolute; left: 22px; top: 8px; width: 146px; height: 138px;
    display: flex; flex-direction: column; align-items: center; justify-content: center; gap: 10px;
    background: radial-gradient(ellipse at 50% 40%, #3c3426, #12100d 80%);
  }
  .brand-dot { width: 34px; height: 34px; border-radius: 50%; border: 2px solid var(--gold); }
  .brand-name { font-size: 20px; font-weight: 700; color: var(--gold); letter-spacing: 0.03em; }

  .nav {
    position: absolute; left: 184px; top: 18px; width: 966px; height: 64px;
    border-radius: 4px;
    background: linear-gradient(var(--bar-top), var(--bar-bottom));
    display: flex; align-items: center; padding-left: 27px;
  }
  .nav a { color: var(--text); text-decoration: none; font-size: 15px; margin-right: 38px; }
  .nav a.active { color: var(--gold); }

  .main {
    position: absolute; left: 184px; top: 93px; width: 966px; height: 756px;
    border-radius: 4px; border: 1px solid var(--panel-edge);
    background:
      radial-gradient(ellipse 300px 260px at 20% 30%, rgba(70,70,70,.25), transparent 70%),
      radial-gradient(ellipse 400px 300px at 75% 80%, rgba(65,65,65,.22), transparent 70%),
      linear-gradient(160deg, var(--panel-a), var(--panel-b));
  }
  .sidebar {
    position: absolute; left: 0; top: 0; width: 214px; height: 100%;
    border-right: 1px solid var(--divider);
  }
  .ad-box {
    position: absolute; left: 10px; top: 37px; width: 196px; height: 66px;
    background: #151515; border: 1px solid #333;
    display: flex; align-items: center; padding-left: 18px; gap: 8px;
    font-size: 24px; color: #3c6f96; letter-spacing: 0;
  }
  .ad-box .mark { width: 22px; height: 22px; border-radius: 50%; background: #3c6f96; }
  .view-switch {
    position: absolute; left: 16px; top: 140px; width: 171px; height: 33px;
    border-radius: 4px; background: linear-gradient(#ffffff, #e4e4e4);
    font-size: 11px; color: #666; display: flex; align-items: center; justify-content: center; gap: 4px;
  }
  .view-switch a { color: var(--gold); }
  .side-note { position: absolute; left: 16px; top: 207px; width: 185px; font-size: 13.5px; line-height: 21px; }
  .side-note h3 { color: var(--gold); font-size: 13.5px; font-weight: 400; margin-bottom: 21px; }

  .content { position: absolute; left: 230px; top: 0; width: 700px; }
  .content h1 { position: absolute; top: 20px; font-size: 27px; font-weight: 400; color: var(--gold); letter-spacing: 0.03em; white-space: nowrap; }
  .hero {
    position: absolute; top: 68px; width: 644px; height: 426px;
    background: linear-gradient(180deg, var(--photo-top) 0%, var(--photo-mid) 45%, var(--photo-low) 100%);
  }
  .copy { position: absolute; top: 511px; width: 700px; font-size: 13.5px; line-height: 21px; }
  .copy p { margin-bottom: 21px; }
  .copy a { color: var(--gold); }

  .footer {
    position: absolute; left: 184px; top: 870px; width: 966px; height: 65px;
    border-radius: 4px; background: linear-gradient(var(--bar-top), var(--bar-bottom));
    font-size: 11px; color: var(--muted);
  }
  .footer-left { position: absolute; left: 18px; top: 37px; display: flex; align-items: center; gap: 5px; }
  .footer-right { position: absolute; right: 6px; top: 35px; }
  .print-icon { width: 12px; height: 11px; }
</style>
</head>
<body>
  <div class="brand">
    <span class="brand-dot"></span>
    <span class="brand-name">FORNVALT</span>
  </div>

  <nav class="nav">
    <a class="active" href="#">Start</a>
    <a href="#">Kontakt</a>
    <a href="#">Unser Produkt</a>
    <a href="#">Preise</a>
    <a href="#">Partner</a>
    <a href="#">Ihr Weg zum Maßschuh</a>
  </nav>

  <main class="main">
    <aside class="sidebar">
      <div class="ad-box"><span class="mark"></span>Webova</div>
      <div class="view-switch">Ansicht: <a href="#">Galerie</a> | <a href="#">Liste</a></div>
      <div class="side-note">
        <h3>Platz für weitere Inhaltselement</h3>
        <p>Es erscheint unterhalb des Menüs der zweiten Ebene. Die Webova Werbebox darüber bitte wegdenken.</p>
      </div>
    </aside>

    <section class="content">
      <h1>Maßschuhe à la carte.</h1>
      <div class="hero" role="img" aria-label="Foto: braune Budapester Maßschuhe in einer Reihe auf einer weiß gedeckten Tafel mit Gläsern"></div>
      <div class="copy">
        <p>Was dürfen wir servieren?</p>
        <p>Von schlicht und elegant, klassisch bis sportlich, trendig oder bequem:<br>
        Wir können Ihnen jeden Wunsch erfüllen.<br>
        Sei es der Nachbau eines Lieblingsschuhs, der nicht mehr erhältlich ist,<br>
        seien es Probleme mit Konfektionsschuhen<br>
        oder ausgefallene Wünsche hinsichtlich Farbe, Form oder Material:</p>
        <p>Wir helfen Ihnen gerne weiter!</p>
        <p>Natürlich halten wir auch schon <a href="#">Menüvorschläge</a> bereit.</p>
      </div>
    </section>
  </main>

  <footer class="footer">
    <div class="footer-left">
      <span>Impressum</span> |
      <svg class="print-icon" viewBox="0 0 12 11"><rect x="3" y="0" width="6" height="4" fill="#fff"/><rect x="0" y="4" width="12" height="5" fill="#ccc"/><rect x="3" y="7" width="6" height="4" fill="#fff"/></svg>
      <span>Druckversion</span> | <span>Sitemap</span>
    </div>
    <div class="footer-right">Webova-Logout | Bearbeiten</div>
  </footer>
</body>
</html>
```